Business Card Design Project

I need a business card designed from scratch. I have an existing logo that I can upload in Illustrator for modification or redesign.

The Company is called Ranking Oracles http://rankingoracles.com.au and we provide Search Engine Optimization services to Australian businesses. The current logo signifies an increase in visitors, profits etc...

There are no restrictions as to the redesign - colours, style etc are all open to change.

Cards will be full colour and one sided printed at http://www.cardmillo.com.au so check their requirements for file format and sizes etc.

I will expect all original files upon completion of project.

Target Market(s)

Any business with a web site looking to improve their search engine rankings

Industry/Entity Type

Business

Requirements
Must have
• I like modern, sleek designs. Clean, not fussy, uncluttered.

```html
<!DOCTYPE html>
<html lang="en">
<head>
<meta charset="utf-8">
<title>Ranking Oracles – Business Card</title>
<link rel="stylesheet" href="https://fonts.googleapis.com/css2?family=Open+Sans:wght@300;400;700;800&display=swap">
<style>
  :root {
    --page-bg: #e6e7e9;
    --card-white: #ffffff;
    --band-blue: #1574bb;
    --brand-blue: #1b6fb5;
    --accent-yellow: #f6c320;
    --text-grey: #6b6d70;
    --text-white: #ffffff;
  }
  * { box-sizing: border-box; margin: 0; padding: 0; }
  html, body {
    width: 1200px;
    height: 900px;
    overflow: hidden;
    background: var(--page-bg);
    font-family: "Open Sans", Arial, sans-serif;
  }
  .card {
    position: absolute;
    left: 80px;
    top: 135px;
    width: 1040px;
    height: 630px;
    background: var(--card-white);
    box-shadow: 0 12px 30px rgba(0, 0, 0, 0.18);
    overflow: hidden;
  }
  .card-holder {
    position: absolute;
    right: 60px;
    top: 48px;
    text-align: right;
  }
  .holder-name {
    color: var(--brand-blue);
    font-weight: 700;
    font-size: 38px;
    line-height: 1.1;
  }
  .holder-title {
    color: var(--text-grey);
    font-weight: 400;
    font-size: 25px;
    margin-top: 6px;
    letter-spacing: 0.3px;
  }
  .brand {
    position: absolute;
    left: 62px;
    top: 300px;
    display: flex;
    align-items: center;
    gap: 18px;
  }
  .brand-dot {
    width: 44px;
    height: 44px;
    border-radius: 50%;
    background: var(--accent-yellow);
  }
  .brand-name {
    color: var(--brand-blue);
    font-weight: 800;
    font-size: 52px;
    line-height: 1;
    letter-spacing: -0.5px;
  }
  .contact-band {
    position: absolute;
    left: 0;
    bottom: 0;
    width: 100%;
    height: 190px;
    background: var(--band-blue);
  }
  .contact-list {
    list-style: none;
    position: absolute;
    left: 58px;
    top: 34px;
  }
  .contact-item {
    display: flex;
    align-items: center;
    gap: 20px;
    color: var(--text-white);
    font-size: 26px;
    font-weight: 400;
    line-height: 42px;
  }
  .contact-icon {
    width: 26px;
    height: 26px;
    flex: none;
  }
</style>
</head>
<body>
  <main class="card">
    <header class="card-holder">
      <h1 class="holder-name">Dean Harlow</h1>
      <p class="holder-title">Internet Marketing Consultant</p>
    </header>

    <div class="brand">
      <span class="brand-dot" aria-hidden="true"></span>
      <span class="brand-name">Ranking Oracles</span>
    </div>

    <section class="contact-band">
      <ul class="contact-list">
        <li class="contact-item">
          <svg class="contact-icon" viewBox="0 0 26 26" aria-hidden="true">
            <path d="M3 9c0-3 4-5 10-5s10 2 10 5v2h-6V9h-8v2H3z" fill="var(--accent-yellow)"/>
            <path d="M7 12h12l3 9H4z" fill="var(--accent-yellow)"/>
            <circle cx="13" cy="16.5" r="2.6" fill="var(--band-blue)"/>
          </svg>
          <span>1300 555 284</span>
        </li>
        <li class="contact-item">
          <svg class="contact-icon" viewBox="0 0 26 26" aria-hidden="true">
            <rect x="3" y="6" width="20" height="14" fill="none" stroke="var(--accent-yellow)" stroke-width="2"/>
            <path d="M3 6l10 8 10-8" fill="none" stroke="var(--accent-yellow)" stroke-width="2"/>
          </svg>
          <span>dean@rankingoracles.com.au</span>
        </li>
        <li class="contact-item">
          <svg class="contact-icon" viewBox="0 0 26 26" aria-hidden="true">
            <g fill="none" stroke="var(--accent-yellow)" stroke-width="2">
              <circle cx="13" cy="13" r="10"/>
              <ellipse cx="13" cy="13" rx="4.5" ry="10"/>
              <path d="M3 13h20M5 8h16M5 18h16"/>
            </g>
          </svg>
          <span>www.rankingoracles.com.au</span>
        </li>
      </ul>
    </section>
  </main>
</body>
</html>
```